Looking for an Innovative Print Design (Service Directory)

We need a new design for our advertisement within a printed colour services directory.

We are a compensation law firm called Velbrook Compensation Lawyers. Feel free to take a browse of our website www.velbrooklegal.com.au to get an idea of what we do and the kind of firm we are.

We are in the process of redeveloping our website and as such, so please don't adhere to the design principles of the current site- impress us with your originality!

On top of any editable formats, your final submissions must include a .pdf copy.
The same design will need to be presented in two dimensions:

- 154mm x 118mm (B1/B2 Half Page);
- 175mm x 113mm (B4 Half Page).

[For more information refer to attached Pdf.]

We have attached for you a few examples of other firms' designs (Sample1,2,3). These are by no means good, or what we're after, it's just to provide you with an idea of what sort of advertisements go into the service directory.

Hi all,

We want to emphasise that a priority of the design is that it must look:
• Professional
• Sophisticated
Please do not hesitate to use completely different colour schemes to the ones that are on our website- as we have said, our website will change in the near future, so cohesion between the current project and the website is not necessary!

Thanks!

Thank you for your submissions so far. There are some great ideas hidden in there. 

An issue we are having is that most of you are conforming to the same understanding of what it should look like. Remember that there is NO NEED to be bound by the image of firm as is. That is, feel free to use a different colour logo.

For inspiration, we relate well to the design aesthetics of: http://www.tinfernstudio.co.uk/

Look forward to seeing your 'out of the box' submissions. 

Reason: We've received a large amount of fantastic designs. However, what we're really looking for is something original. Please feel free to think outside the box (the final design doesn't need to look like a print ad), and construct a design that is completely incongruous with our website! While we do appreciate a minimalistic design, we have yet to receive something that really grabs your attention with its visuals. We're not sure but this may or may not be achieved with a full colour design. Thanks for all your submissions- they all have some features that really click with us. We look forward to the next wave of submissions!

Target Market(s)

We have various target markets, including mainly families, elderly people, blue collar workers.

These are individuals who are looking for assistance. They feel helpless or wronged.

Keep in mind that the people accessing these are those who prefer going to a printed directory rather than using a google search.

Industry/Entity Type

Law Firm

Font styles to use
Serif
Sans Serif

Requirements
Must have
• - Our name 'Velbrook Compensation Lawyers'
- Our logo (attached as logo.eps, logo.png, and logo.tif)
- Must include phone number as 1300 XXX XXX (this must be prominent)
- Must include the following service areas in these words: Motor vehicle claims, medical claims, superannuation claims, Workplace claims, negligence claims
- Our email address: info@velbrooklegal.com.au
- Our website address: www.velbrooklegal.com.au
- The following catchphrases: '98% success rate', and 'No win no fee' in those words
- Our location '412 Carvel Lane, Smithville, SYDNEY'
- For sizing dimensions, we need one in 154mm x 118mm and also a design in 175mm x 113mm (B4 Half Page) [refer to pdf attached]
Nice to have
• - Text indicating free initial consulatation
- Professional colour scheme
- As our website will be changed, do not worry about making the advertisement cohesive with our website design
- We want the design to be modern, but still professional
- Clean typeface
- No gradient colour scheme
- When designing, if you are looking to place more text onto the advertisement, these may be some considerations (feel free to change the wording): Accredited specialists, home and hospital visits

```html
<!DOCTYPE html>
<html lang="en">
<head>
<meta charset="utf-8">
<title>Velbrook Compensation Lawyers – Directory Advertisement</title>
<link rel="stylesheet" href="https://fonts.googleapis.com/css2?family=Roboto:wght@300;400&family=Roboto+Condensed:ital,wght@0,700;1,400&display=swap">
<style>
  :root {
    --orange: #f0701f;
    --navy: #2a2f3d;
    --grey: #6d6f73;
    --paper: #ffffff;
    --suit-dark: #24272d;
    --suit-mid: #4b5058;
    --shirt: #c9ccd2;
  }
  * { margin: 0; padding: 0; box-sizing: border-box; }
  html, body { width: 1200px; height: 774px; overflow: hidden; background: var(--paper); }
  .ad { position: relative; width: 1200px; height: 774px; background: var(--paper); overflow: hidden; }

  .hero-photo {
    position: absolute; left: 384px; top: 0; width: 816px; height: 643px;
    background: linear-gradient(90deg, var(--suit-dark) 0%, var(--suit-mid) 30%, var(--shirt) 50%, var(--suit-mid) 70%, var(--suit-dark) 100%);
  }

  .headline {
    position: absolute; left: 180px; top: 22px;
    font-family: "Roboto", sans-serif; font-weight: 400;
    font-size: 102px; line-height: 1; color: var(--orange);
    letter-spacing: -1px; white-space: nowrap;
  }
  .headline sup { font-size: 52px; vertical-align: top; position: relative; top: 6px; }

  .services {
    position: absolute; right: 836px; top: 148px; list-style: none; text-align: right;
    font-family: "Roboto Condensed", sans-serif; font-weight: 700;
    font-size: 27px; line-height: 38px; color: var(--navy);
  }
  .extras {
    position: absolute; right: 836px; top: 424px; text-align: right;
    font-family: "Roboto Condensed", sans-serif; font-style: italic; font-weight: 400;
    font-size: 23px; line-height: 52px; color: var(--navy);
  }
  .no-win {
    position: absolute; right: 836px; top: 556px;
    font-family: "Roboto Condensed", sans-serif; font-weight: 700;
    font-size: 46px; line-height: 1; color: var(--navy); white-space: nowrap;
  }
  .phone {
    position: absolute; left: 390px; top: 530px;
    font-family: "Roboto", sans-serif; font-weight: 400;
    font-size: 106px; line-height: 1; color: var(--orange); white-space: nowrap;
  }

  .brand { position: absolute; left: 18px; top: 678px; display: flex; align-items: center; gap: 16px; }
  .brand-dot { width: 64px; height: 64px; border-radius: 50%; background: var(--orange); flex: none; }
  .brand-name {
    font-family: "Roboto", sans-serif; font-weight: 400; font-size: 26px;
    letter-spacing: 2px; color: var(--grey); text-transform: uppercase; white-space: nowrap;
  }

  .contact {
    position: absolute; right: 24px; top: 664px; text-align: right;
    font-family: "Roboto", sans-serif; font-weight: 400; line-height: 36px;
  }
  .contact .address { font-size: 18px; letter-spacing: 4px; color: var(--navy); text-transform: uppercase; }
  .contact .email, .contact .web { font-size: 20px; color: var(--orange); }
</style>
</head>
<body>
<div class="ad">
  <div class="hero-photo" role="img" aria-label="Photograph of a man in a dark suit pulling open his shirt, superhero style"></div>

  <h1 class="headline">98<sup>%</sup> SUCCESS RATE</h1>

  <ul class="services">
    <li>MOTOR VEHICLE CLAIMS</li>
    <li>NEGLIGENCE CLAIMS</li>
    <li>MEDICAL CLAIMS</li>
    <li>SUPERANNUATION CLAIMS</li>
    <li>NEGLIGENCE CLAIMS</li>
    <li>WORKPLACE CLAIMS</li>
  </ul>

  <div class="extras">
    <p>ACCREDITED SPECIALISTS</p>
    <p>HOME AND HOSPITAL VISITS</p>
  </div>

  <p class="no-win">NO WIN. NO FEE.</p>
  <p class="phone">1300 XXX XXX</p>

  <div class="brand">
    <span class="brand-dot"></span>
    <span class="brand-name">Velbrook Compensation Lawyers</span>
  </div>

  <address class="contact" style="font-style: normal;">
    <p class="address">412 Carvel Lane Smithville, Sydney</p>
    <p class="email">info@velbrooklegal.com.au</p>
    <p class="web">www.velbrooklegal.com.au</p>
  </address>
</div>
</body>
</html>
```